Pop punk gig poster design!

In need of an amazing poster design for a gig We are organising, the genre is pop punk, and will be an all ages gig. I need to it bold, random and capture the eye of any bypasses, and make people want to go to the gig just because the poster is awesome! The event will be called "A glimpse of neon" and will consist of three bands and an acoustic set to open. All the bands are full of energy and create an unreal ambiance during there shows, I would like to capture that in the poster. Open to anything spectacular, the sky is the limit.

• I need to have the name of the event "A Glimpse Of Neon"
Band names(in this order):
-Fold the Lantern
-Velvet Orchard
-Gemwick's Oar
-Lunetta Pribble

Date: Saturday 10th November 2012
Time: 5:15pm
Venue: The Quill, 47 Marrowfen street, West End, QLD 4101
Ticket price: $10+bf online
$15 at the door.
Free BBQ

```html
<!DOCTYPE html>
<html lang="en">
<head>
<meta charset="utf-8">
<title>A Glimpse Of Neon — Gig Poster</title>
<link rel="stylesheet" href="https://fonts.googleapis.com/css2?family=Audiowide&family=Metal+Mania&family=Cinzel:wght@900&family=Russo+One&family=Oswald:wght@500&display=swap">
<style>
  :root {
    --wall-light: #4a4658;
    --wall-mid: #2a2735;
    --wall-dark: #121019;
    --guitar-light: #b0289a;
    --guitar-dark: #4a1a7a;
    --title-neon: #ff3fb4;
    --title-glow: #ff0090;
    --tagline-neon: #8dff3a;
    --tagline-glow: #3cff00;
    --band-cream: #fff27a;
    --band-outline: #0d0d0d;
    --ticket-neon: #3ff2ff;
    --info-ink: #ffffff;
    --bbq-neon: #ff9a1f;
    --rule: #3ff2ff;
  }
  * { margin: 0; padding: 0; box-sizing: border-box; }
  html, body { width: 848px; height: 1200px; overflow: hidden; background: var(--wall-mid); }
  .poster { position: relative; width: 848px; height: 1200px; overflow: hidden; }
  .wall-texture {
    position: absolute; inset: 0;
    background: radial-gradient(ellipse at 45% 40%, var(--wall-light) 0%, var(--wall-mid) 60%, var(--wall-dark) 100%);
  }
  .guitar-art {
    position: absolute;
    left: -85px; top: 455px;
    width: 1030px; height: 210px;
    border-radius: 150px 50px 50px 150px;
    transform: rotate(-39deg);
    background: linear-gradient(180deg, var(--guitar-light), var(--guitar-dark));
    box-shadow: 0 0 30px rgba(255, 63, 180, .45);
  }
  .event-title {
    position: absolute; left: 0; right: 0; top: 88px;
    text-align: center;
    font-family: "Audiowide", sans-serif; font-weight: 400;
    font-size: 56px; letter-spacing: 2px; line-height: 1;
    color: var(--title-neon);
    text-transform: uppercase; white-space: nowrap;
    text-shadow: 0 0 6px var(--title-glow), 0 0 18px var(--title-glow);
  }
  .title-rule {
    position: absolute; left: 6px; right: 6px; top: 150px;
    height: 3px; background: var(--title-neon);
    box-shadow: 0 0 8px var(--title-glow);
  }
  .tagline {
    position: absolute; left: 18px; top: 205px;
    font-family: "Metal Mania", cursive;
    font-size: 66px; line-height: 1;
    color: var(--tagline-neon);
    text-transform: uppercase; white-space: nowrap;
    transform: rotate(8deg); transform-origin: left center;
    text-shadow: 2px 2px 0 #000, 0 0 14px var(--tagline-glow);
  }
  .lineup {
    position: absolute; left: 290px; top: 372px;
    list-style: none;
    transform: rotate(9deg); transform-origin: left top;
  }
  .lineup li {
    font-family: "Cinzel", serif; font-weight: 900;
    font-size: 44px; line-height: 90px;
    color: var(--band-cream);
    text-transform: uppercase; white-space: nowrap;
    text-shadow: -2px -2px 0 var(--band-outline), 2px -2px 0 var(--band-outline),
                 -2px 2px 0 var(--band-outline), 2px 2px 0 var(--band-outline),
                 0 0 14px rgba(255, 242, 122, .6);
  }
  .lineup li:nth-child(2) { margin-left: -24px; }
  .lineup li:nth-child(3) { margin-left: -48px; }
  .lineup li:nth-child(4) { margin-left: -72px; }
  .tickets {
    position: absolute; right: 10px; top: 876px;
    text-align: right;
    font-family: "Russo One", sans-serif;
    font-size: 29px; line-height: 40px;
    color: var(--ticket-neon);
    text-transform: uppercase; font-style: italic;
    text-shadow: 0 0 8px rgba(63, 242, 255, .7);
  }
  .tickets p { border-bottom: 2px solid var(--rule); padding-left: 10px; }
  .event-details {
    position: absolute; left: 34px; top: 1008px;
    font-family: "Oswald", sans-serif; font-weight: 500;
    font-size: 27px; line-height: 45px;
    color: var(--info-ink);
    text-transform: uppercase;
    text-shadow: 1px 1px 2px #000;
  }
  .free-bbq {
    position: absolute; right: 14px; top: 1140px;
    font-family: "Russo One", sans-serif;
    font-size: 34px; line-height: 1;
    color: var(--bbq-neon);
    text-transform: uppercase; font-style: italic;
    text-shadow: 0 0 10px var(--bbq-neon);
  }
</style>
</head>
<body>
<main class="poster">
  <div class="wall-texture" role="img" aria-label="Dark brick wall texture"></div>
  <div class="guitar-art" role="img" aria-label="Neon-toned electric guitar silhouette set diagonally across the wall"></div>

  <h1 class="event-title">A Glimpse Of Neon</h1>
  <div class="title-rule"></div>

  <p class="tagline">Let us rock....</p>

  <ul class="lineup">
    <li>-Fold the Lantern</li>
    <li>-Velvet Orchard</li>
    <li>-Gemwick's Oar</li>
    <li>-Lunetta Pribble</li>
  </ul>

  <div class="tickets">
    <p>Ticket price: $10+bf online</p>
    <p>$15 at the door</p>
  </div>

  <div class="event-details">
    <p>Date: Saturday 10th November 2012</p>
    <p>Time: 5:15pm</p>
    <p>Venue: The Quill, 47 Marrowfen Street,</p>
    <p>West End, QLD 4101</p>
  </div>

  <p class="free-bbq">Free BBQ</p>
</main>
</body>
</html>
```